2-page insert to artglass Catalogue

We need a inner page design for our 2014 product catalogue. There are two pages to be work on- the first two pages you would see when you open the catalog. We manufacture functional glass art products. All our products were hand blowned using the traditional methods and techiques in our own factory.

Our products are artfully hand-crafted, and colorful in design. We take everyday items, and express it through our medium in a art+ function idea. So the purpose of these 2 pages is to share with the readers, the thoughts, philosphy, values, and anthenticity of craftmanship behind each product.

Here are some example websites that have a similar introduction. What these introduction sections in these websites in purpose is what we want these two pages to serve in our catalog. To give a sense of authenticity, to share with the history and craftmanship behind the products, highlight value and selling points of the medium.

http://www.vendrolumen.com/en/company.aspx
http://www.ombrafa.in/wp-content/uploads/2013/10/Tulo%20Vetrano_Contemporary%202013.pdf

Target Market(s)

lighting retailers, art product retailers, furniture store, interior designers.

Industry/Entity Type

It Company

Requirements
Must have
• The content of the two pages should include the 5 sections which show our cability, specialty and product charactors as below:
1. our creativity & experience (should show our creativity in our product design, the unique details of our design)
2. born in fire (our glass product were made through fire in very hight temprature fire oven)
3. function + art(this section shows that our produts are combinations of functional and artistic designing)
4. dancing in colors(this section should be colorful and cheerful)
5. tell your own story(for our wall art plates for wall decor designs)

Instruction:
A4 format.
1. The Instruction is in the Word file attached.
The intrduction shows which picsbelong to which content section. Please feel free to use the pictures creatively.
2. Product and setting pics attached.
3. Text content in the Word file.
Nice to have
• Room for short phases and brief descriptions for the five sections described above.
Should not have
• pictures other than our own product pics.

```html
<!DOCTYPE html>
<html lang="en">
<head>
<meta charset="utf-8">
<title>Lumo Glass – Catalogue Introduction Spread</title>
<link rel="stylesheet" href="https://fonts.googleapis.com/css2?family=Roboto:wght@300&family=Arimo:wght@400&display=swap">
<style>
  :root {
    --canvas: #ffffff;
    --page-dark: #1c1a1a;
    --heading: #e6e3e0;
    --body-text: #ece9e6;
    --fire-deep: #7a2a05;
    --fire-bright: #f39a1c;
  }
  * { margin: 0; padding: 0; box-sizing: border-box; }
  html, body { width: 1200px; height: 998px; overflow: hidden; background: var(--canvas); }
  .spread { position: relative; width: 1200px; height: 998px; }
  .page { position: absolute; top: 125px; width: 578px; height: 746px; background: var(--page-dark); overflow: hidden; }
  .page--left { left: 15px; }
  .page--right { left: 607px; }
  .photo { position: absolute; }
  .section-title {
    position: absolute; font-family: 'Roboto', 'Helvetica Neue', Arial, sans-serif;
    font-weight: 300; font-size: 21px; line-height: 22px; color: var(--heading);
    white-space: nowrap;
  }
  .section-copy {
    position: absolute; font-family: 'Arimo', Arial, sans-serif;
    font-size: 9.2px; line-height: 13.2px; color: var(--body-text);
    white-space: nowrap; letter-spacing: -0.05px;
  }

  /* left page */
  .photo--glassblowing { left: 147px; top: 0; width: 285px; height: 186px; background: linear-gradient(120deg, #e8e8e8 0%, #9a9a9a 40%, #3a3a3a 70%, #bdbdbd 100%); }
  .photo--furnace { left: 432px; top: 0; width: 146px; height: 186px; background: radial-gradient(ellipse at 45% 60%, #fff2b0 0%, var(--fire-bright) 30%, #c84a08 55%, var(--fire-deep) 75%, #120604 100%); }
  .photo--sculpture { left: 432px; top: 186px; width: 146px; height: 187px; background: linear-gradient(180deg, #f4f4f4 0%, #e69a3a 35%, #ef8a1a 60%, #eeeeee 100%); }
  .photo--living-room { left: 147px; top: 373px; width: 285px; height: 186px; background: linear-gradient(180deg, #d9cfbf 0%, #c9bca6 55%, #3a3634 70%, #8a6a40 100%); }

  .title--creativity { left: 13px; top: 11px; }
  .copy--creativity { left: 13px; top: 57px; }
  .title--function { left: 150px; top: 198px; }
  .copy--function { left: 150px; top: 224px; }
  .title--story { left: 9px; top: 376px; }
  .copy--story { left: 13px; top: 430px; }

  /* right page */
  .photo--glass-knot { left: 150px; top: 0; width: 428px; height: 746px; background: linear-gradient(100deg, var(--page-dark) 0%, #4a4846 25%, #cfcfcf 50%, #8e8e8e 70%, #e6e6e6 85%, #5a5a5a 100%); }
  .photo--flame { left: 0; top: 0; width: 143px; height: 186px; background: radial-gradient(ellipse at 40% 35%, #ffe08a 0%, var(--fire-bright) 30%, #d0520c 55%, #1e0d05 85%); }
  .photo--wall-plates { left: 0; top: 373px; width: 216px; height: 186px; background: linear-gradient(135deg, #f29a2a 0%, #e65a1a 35%, #8a84d8 65%, #f6f6f6 100%); }
  .photo--vase { left: 216px; top: 559px; width: 145px; height: 187px; background: radial-gradient(ellipse at 50% 55%, #f5c21c 0%, #f0a818 40%, #e0dede 75%); }
  .text-panel { position: absolute; background: var(--page-dark); }
  .text-panel--fire { left: 143px; top: 0; width: 200px; height: 186px; }
  .text-panel--colors { left: 0; top: 186px; width: 216px; height: 187px; }
  .text-panel--base { left: 0; top: 559px; width: 216px; height: 187px; }

  .title--fire { left: 153px; top: 11px; }
  .copy--fire { left: 153px; top: 35px; }
  .title--colors { left: 13px; top: 196px; }
  .copy--colors { left: 13px; top: 227px; }
</style>
</head>
<body>
<div class="spread">
  <section class="page page--left">
    <div class="photo photo--glassblowing" role="img" aria-label="Black and white photo of a glass artist shaping a blown glass disc on a pipe"></div>
    <div class="photo photo--furnace" role="img" aria-label="Glowing furnace opening with bright orange flames"></div>
    <div class="photo photo--sculpture" role="img" aria-label="Orange art glass head sculpture on a clear glass base"></div>
    <div class="photo photo--living-room" role="img" aria-label="Modern living room with colourful glass wall plates above white sofas"></div>

    <h2 class="section-title title--creativity">Creativity<br>&amp; Experience</h2>
    <p class="section-copy copy--creativity">Lumo Glass products are inspired<br>by other artists, furniture and<br>lighting design, and popular art.<br>The creativity of our glass art is<br>in the expression of this color<br>and design elements seen as<br>all of us go through each day.<br>Our artist's experience with<br>their craft provides a way<br>to interpret all of our<br>environment's inputs that<br>provide our inspiration.</p>

    <h2 class="section-title title--function">Function &amp; Art</h2>
    <p class="section-copy copy--function">The combination of function and art answers the retailer's<br>need for products that create both the impulse to buy and a<br>reason to buy.&nbsp; This joining of beauty and function in our vases<br>and bowls, distinctive lighting and other items make it easy to<br>convey the total acceptance of the art within the home.&nbsp; Many<br>Lumo Glass products offer the ability to provide both a beautiful<br>piece of art and a purpose for placement in every home.<br>Or, for the simple love of art, the splash of bold or muted<br>colors available can solve the simple lust to make an<br>environment a more pleasant place to be.</p>

    <h2 class="section-title title--story">Tell your own<br>story...</h2>
    <p class="section-copy copy--story">Lumo Glass provides that final<br>piece to bring a design<br>together, or a focus on which to<br>build a room's theme.&nbsp; Colors<br>themselves provide the design<br>cues that tie a room together<br>– the rich deep colors to<br>alleviate a modern room's bare<br>white walls, spicy reds and<br>yellow to fire up urban spaces,<br>purples to add serene elements<br>to complex spaces, limes<br>and cyan to bring freshness<br>to cottage themes, or deeper<br>trustful blues to add power to<br>traditional themes.&nbsp; All of these<br>are Lumo Glass.</p>
  </section>

  <section class="page page--right">
    <div class="photo photo--glass-knot" role="img" aria-label="Large clear twisted glass rope sculpture against a dark background"></div>
    <div class="text-panel text-panel--fire"></div>
    <div class="text-panel text-panel--colors"></div>
    <div class="text-panel text-panel--base"></div>
    <div class="photo photo--flame" role="img" aria-label="Flames rising from a glass furnace"></div>
    <div class="photo photo--wall-plates" role="img" aria-label="Orange, green and purple blown glass wall plates"></div>
    <div class="photo photo--vase" role="img" aria-label="Yellow art glass vase with colourful abstract inlays"></div>

    <h2 class="section-title title--fire">Born in Fire</h2>
    <p class="section-copy copy--fire">The methods of the art are simple: fire and<br>silica combine in a liquid that is formed by<br>tools whose concept is almost 2000 years<br>old.&nbsp; Free-blowing techniques to make glass<br>have evolved from the creation of purely<br>functional items centuries ago into an artist's<br>tool used to create beautiful accessories<br>you see in our Lumo Glass product line.</p>

    <h2 class="section-title title--colors">Dancing in Colors</h2>
    <p class="section-copy copy--colors">That simple splash of color created<br>by Lumo Glass art provides the accent<br>that define an environment.&nbsp; Colorful<br>glass art is a solution to a black<br>and white world, enhancing the<br>emotion in a room, and bringing<br>a multitude of palette alternatives<br>to the designer's tool box.<br>Life is too short for beige.</p>
  </section>
</div>
</body>
</html>
```